Change lives by changing education

We need stationery (business cards, letterhead, envelopes, with compliments slips and A4 display folders) that will support us to make an impact in education through recruitment and consultancy services. All our consultants are highly experienced with more than 20 years of industry experience and are all passionate about improving education by attracting the brightest and the best. We believe strongly in empowering students to take control of their own learning and turn their own ideas into reality.
We work in the independent/private school space which can be thought of as conservative, but they are just starting to "get with the times" and be more progressive, so the message has to carry across that space.We are a younger firm, but one of the few who has experienced educators running the show. Help us to make a difference to the world please!

Target Market(s)

Principals and School Board members

Industry/Entity Type

Business

Requirements
Must have
• The logo
Nice to have
• Use of the logo colours Indigo and a specific type of green
Should not have
• Nothing tacky to do with education, incl quills, pens, mortar boards, books

```html
<!DOCTYPE html>
<html lang="en">
<head>
<meta charset="utf-8">
<title>Calder Consulting – Presentation Folder</title>
<link href="https://fonts.googleapis.com/css2?family=Open+Sans:wght@400;600;700&display=swap" rel="stylesheet">
<style>
  :root {
    --indigo: #2b2a6b;
    --green: #5b8a33;
    --lavender: #c5c3de;
    --sage: #d4dcc9;
    --paper: #ffffff;
    --fold: #e6e6e6;
    --backdrop: #b4b4b4;
    --slit: #c0392b;
    --ink: #333333;
  }
  * { box-sizing: border-box; margin: 0; padding: 0; }
  html, body {
    width: 1021px; height: 1200px; overflow: hidden;
    background: var(--backdrop);
    font-family: "Open Sans", Arial, sans-serif;
  }
  .canvas { position: relative; width: 1021px; height: 1200px; }

  .spread { position: absolute; left: 105px; width: 810px; height: 540px; display: flex; }
  .spread--outside { top: 30px; }
  .spread--inside { top: 596px; }
  .panel {
    position: relative; width: 405px; height: 540px;
    background: var(--paper); overflow: hidden;
  }
  .panel + .panel { border-left: 1px solid var(--fold); }

  /* wordmark */
  .wordmark { display: flex; align-items: center; gap: 7px; color: var(--indigo); font-weight: 600; white-space: nowrap; }
  .wordmark__dot { border-radius: 50%; background: var(--green); flex: none; }
  .wordmark--lg { font-size: 21px; letter-spacing: 0.5px; }
  .wordmark--lg .wordmark__dot { width: 14px; height: 14px; }
  .wordmark--md { font-size: 16px; }
  .wordmark--md .wordmark__dot { width: 11px; height: 11px; }
  .wordmark--sm { font-size: 11px; }
  .wordmark--sm .wordmark__dot { width: 8px; height: 8px; }

  /* decorative leaf fields */
  .leaf-field { position: absolute; border-radius: 50% 50% 0 0; }
  .leaf-field--faint {
    left: -10px; bottom: 0; width: 420px; height: 360px;
    background: radial-gradient(ellipse at 50% 100%, rgba(255,255,255,0) 18%, rgba(197,195,222,0.75) 40%, rgba(212,220,201,0.6) 70%, rgba(255,255,255,0) 100%);
  }
  .leaf-field--bold {
    right: -10px; bottom: 0; width: 390px; height: 190px;
    background: radial-gradient(ellipse at 60% 100%, rgba(255,255,255,0) 12%, rgba(43,42,107,0.85) 40%, rgba(91,138,51,0.8) 68%, rgba(255,255,255,0) 100%);
  }
  .leaf-field--pocket-left {
    left: 0; bottom: 0; width: 190px; height: 130px; border-radius: 0 100% 0 0;
    background: radial-gradient(ellipse at 0% 100%, rgba(43,42,107,0.85) 25%, rgba(91,138,51,0.75) 60%, rgba(255,255,255,0) 100%);
  }
  .leaf-field--pocket-right {
    right: 0; bottom: 0; width: 200px; height: 140px; border-radius: 100% 0 0 0;
    background: radial-gradient(ellipse at 100% 100%, rgba(43,42,107,0.85) 25%, rgba(91,138,51,0.75) 60%, rgba(255,255,255,0) 100%);
  }
  .leaf-field--pocket-faint {
    width: 110px; height: 70px; border-radius: 50%;
    background: radial-gradient(ellipse at 50% 50%, rgba(197,195,222,0.8) 20%, rgba(212,220,201,0.6) 60%, rgba(255,255,255,0) 100%);
  }

  /* back cover */
  .back-contact { position: absolute; left: 40px; bottom: 28px; display: flex; align-items: center; gap: 10px; }
  .back-contact__rule { width: 1px; height: 48px; background: var(--ink); opacity: 0.5; }
  .back-contact__list { list-style: none; font-size: 6.5px; line-height: 1.45; color: var(--ink); }
  .back-contact__list li { display: flex; align-items: center; gap: 4px; }
  .back-contact__list .gap { margin-top: 3px; }
  .back-contact__list .address { color: var(--indigo); }
  .mini-icon { width: 6px; height: 6px; flex: none; }

  /* front cover */
  .front-logo { position: absolute; top: 40px; right: 28px; }

  /* inside spread */
  .flap-line { position: absolute; top: 0; width: 1px; height: 350px; background: var(--fold); }
  .flap-line--left { left: 24px; }
  .flap-line--right { right: 24px; }
  .notch { position: absolute; top: 198px; width: 32px; height: 44px; background: var(--backdrop); }
  .notch--left { left: -8px; border-radius: 0 22px 22px 0; }
  .notch--right { right: -8px; border-radius: 22px 0 0 22px; }

  .pocket {
    position: absolute; bottom: 0; width: 405px; height: 195px;
    background: var(--paper); overflow: hidden;
    box-shadow: 0 -2px 4px rgba(0,0,0,0.08);
  }
  .pocket--left { left: 0; border-top-right-radius: 22px; border-top: 1px solid var(--fold); }
  .pocket--right { left: 0; border-top-left-radius: 22px; border-top: 1px solid var(--fold); }

  .services { position: absolute; left: 205px; top: 52px; color: var(--ink); }
  .services__title { font-size: 8px; font-weight: 700; color: var(--indigo); margin-bottom: 3px; }
  .services__list { list-style: none; font-size: 6.5px; line-height: 1.7; }
  .services__list li { display: flex; align-items: center; gap: 4px; }
  .pocket-logo--left { position: absolute; left: 200px; top: 140px; }
  .pocket-logo--right { position: absolute; left: 118px; top: 92px; }
  .card-slits { position: absolute; left: 80px; top: 50px; }

  .annotation { position: absolute; right: 80px; top: 1152px; font-size: 17px; letter-spacing: 1px; color: #222; }
  .annotation-lines { position: absolute; left: 0; top: 0; pointer-events: none; }
</style>
</head>
<body>
<main class="canvas">

  <!-- Outside of folder: back cover + front cover -->
  <section class="spread spread--outside">
    <article class="panel panel--back">
      <div class="leaf-field leaf-field--faint" role="img" aria-label="Faint burst of lavender and sage leaves rising from the bottom edge"></div>
      <div class="back-contact">
        <div class="wordmark wordmark--sm"><span class="wordmark__dot"></span>Calder Consulting</div>
        <span class="back-contact__rule"></span>
        <ul class="back-contact__list">
          <li><svg class="mini-icon" viewBox="0 0 10 10"><path d="M2 1h2l1 2-1 1c.5 1 1.5 2 2.5 2.5l1-1 2 1v2c-4 0-7.5-3.5-7.5-7.5z" fill="var(--green)"/></svg>+61 3 9555 0142</li>
          <li><svg class="mini-icon" viewBox="0 0 10 10"><rect x="1" y="3" width="8" height="6" fill="var(--green)"/></svg>+61 3 9555 0187</li>
          <li class="gap"><svg class="mini-icon" viewBox="0 0 10 10"><rect x="1" y="2" width="8" height="6" fill="var(--green)"/></svg>hello@calderconsulting.com.au</li>
          <li><svg class="mini-icon" viewBox="0 0 10 10"><circle cx="5" cy="5" r="4" fill="var(--green)"/></svg>www.calderconsulting.com.au</li>
          <li class="gap address">Suite 4, 18 Elmwood Road</li>
          <li class="address">Kew VIC Australia 3101</li>
        </ul>
      </div>
    </article>
    <article class="panel panel--front">
      <div class="front-logo wordmark wordmark--lg"><span class="wordmark__dot"></span>Calder Consulting</div>
      <div class="leaf-field leaf-field--bold" role="img" aria-label="Burst of indigo and green leaves rising from the bottom edge"></div>
    </article>
  </section>

  <!-- Inside of folder: two pockets -->
  <section class="spread spread--inside">
    <article class="panel panel--inside-left">
      <span class="flap-line flap-line--left"></span>
      <span class="notch notch--left"></span>
      <div class="pocket pocket--left">
        <div class="leaf-field leaf-field--pocket-faint" style="left:290px; top:-8px;" role="img" aria-label="Faint lavender and sage leaf cluster"></div>
        <div class="leaf-field leaf-field--pocket-left" role="img" aria-label="Indigo and green leaf cluster in the corner"></div>
        <div class="services">
          <h3 class="services__title">Our Services</h3>
          <ul class="services__list">
            <li><svg class="mini-icon" viewBox="0 0 10 10"><rect width="10" height="10" fill="var(--green)"/><path d="M2 5l2 2 4-4" stroke="#fff" stroke-width="1.4" fill="none"/></svg>Lorem Ipsum is simply dummy text printing</li>
            <li><svg class="mini-icon" viewBox="0 0 10 10"><rect width="10" height="10" fill="var(--green)"/><path d="M2 5l2 2 4-4" stroke="#fff" stroke-width="1.4" fill="none"/></svg>Typesetting industry. Lorem Ipsum</li>
            <li><svg class="mini-icon" viewBox="0 0 10 10"><rect width="10" height="10" fill="var(--green)"/><path d="M2 5l2 2 4-4" stroke="#fff" stroke-width="1.4" fill="none"/></svg>Industry's standard dummy text ever since the</li>
            <li><svg class="mini-icon" viewBox="0 0 10 10"><rect width="10" height="10" fill="var(--green)"/><path d="M2 5l2 2 4-4" stroke="#fff" stroke-width="1.4" fill="none"/></svg>When an unknown printer took a galley of type</li>
            <li><svg class="mini-icon" viewBox="0 0 10 10"><rect width="10" height="10" fill="var(--green)"/><path d="M2 5l2 2 4-4" stroke="#fff" stroke-width="1.4" fill="none"/></svg>Scrambled it to make a type specimen book.</li>
          </ul>
        </div>
        <div class="pocket-logo--left wordmark wordmark--md"><span class="wordmark__dot"></span>Calder Consulting</div>
      </div>
    </article>
    <article class="panel panel--inside-right">
      <span class="flap-line flap-line--right"></span>
      <span class="notch notch--right"></span>
      <div class="pocket pocket--right">
        <div class="leaf-field leaf-field--pocket-faint" style="left:-10px; top:-6px;" role="img" aria-label="Faint lavender and sage leaf cluster"></div>
        <div class="leaf-field leaf-field--pocket-right" role="img" aria-label="Indigo and green leaf cluster in the corner"></div>
        <svg class="card-slits" width="190" height="110" viewBox="0 0 190 110" aria-hidden="true">
          <g stroke="var(--slit)" stroke-width="1">
            <line x1="0" y1="22" x2="24" y2="0"/>
            <line x1="166" y1="0" x2="190" y2="22"/>
            <line x1="0" y1="88" x2="24" y2="110"/>
            <line x1="166" y1="110" x2="190" y2="88"/>
          </g>
        </svg>
        <div class="pocket-logo--right wordmark wordmark--md"><span class="wordmark__dot"></span>Calder Consulting</div>
      </div>
    </article>
  </section>

  <svg class="annotation-lines" width="1021" height="1200" aria-hidden="true">
    <g stroke="#222" stroke-width="1">
      <line x1="762" y1="1010" x2="840" y2="1148"/>
      <line x1="762" y1="1010" x2="850" y2="1148"/>
    </g>
  </svg>
  <p class="annotation">Place to put Business Cards</p>

</main>
</body>
</html>
```